BRTW Traditional Business Card Project

Please see attached....just a simple business card... on attachment- please use the exact font, style, etc as the attached "Dal Rupert Huxley" card... however, replace with the "Owen Bartholomew Lindqvist" text and address below the card.

```html
<!DOCTYPE html>
<html lang="en">
<head>
<meta charset="utf-8">
<title>Harrow &amp; Vance — Business Card</title>
<link rel="stylesheet" href="https://fonts.googleapis.com/css2?family=Libre+Baskerville:wght@400;700&display=swap">
<style>
  :root {
    --backdrop: #d9dbdf;
    --card: #333a48;
    --ink: #ffffff;
    --ink-soft: #d5d8de;
    --rule: #7a8090;
    --serif: "Libre Baskerville", "Times New Roman", serif;
  }
  * { margin: 0; padding: 0; box-sizing: border-box; }
  html, body { width: 1200px; height: 900px; overflow: hidden; }
  body {
    background: var(--backdrop);
    font-family: var(--serif);
    color: var(--ink);
    display: flex;
    flex-direction: column;
    align-items: center;
    justify-content: center;
    gap: 40px;
  }
  .card {
    position: relative;
    width: 700px;
    height: 400px;
    background: var(--card);
    box-shadow: 0 6px 18px rgba(0,0,0,0.25);
  }
  .firm-mark { text-align: left; }
  .firm-name {
    font-weight: 700;
    font-variant: small-caps;
    letter-spacing: 0.02em;
    line-height: 1;
    white-space: nowrap;
  }
  .firm-tagline {
    font-weight: 400;
    text-transform: uppercase;
    letter-spacing: 0.14em;
    color: var(--ink-soft);
    white-space: nowrap;
  }

  /* back side */
  .card--back .firm-mark {
    position: absolute;
    top: 50%; left: 50%;
    transform: translate(-50%, -50%);
  }
  .card--back .firm-name { font-size: 44px; }
  .card--back .firm-tagline { font-size: 13px; margin-top: 6px; }

  /* front side */
  .card--front .firm-mark {
    position: absolute;
    top: 108px; right: 48px;
  }
  .card--front .firm-name { font-size: 27px; }
  .card--front .firm-tagline { font-size: 8px; margin-top: 4px; }

  .person {
    position: absolute;
    top: 50px; left: 48px;
  }
  .person-name {
    font-size: 26px;
    font-weight: 700;
    font-variant: small-caps;
    letter-spacing: 0.02em;
    line-height: 1;
    white-space: nowrap;
  }
  .person-title {
    font-size: 9px;
    letter-spacing: 0.08em;
    text-transform: uppercase;
    color: var(--ink-soft);
    margin-top: 6px;
  }
  .person-rule {
    width: 44px;
    height: 1px;
    background: var(--rule);
    margin: 16px 0 14px;
  }
  .contact-list { list-style: none; }
  .contact-item {
    display: flex;
    align-items: center;
    gap: 10px;
    font-size: 12px;
    color: var(--ink-soft);
    line-height: 20px;
  }
  .contact-icon {
    width: 11px; height: 11px;
    fill: var(--ink-soft);
    flex: none;
  }
  .address {
    position: absolute;
    right: 48px; bottom: 46px;
    text-align: right;
    font-size: 15px;
    font-style: normal;
    letter-spacing: 0.02em;
    text-transform: uppercase;
    color: var(--ink-soft);
    line-height: 1.55;
  }
</style>
</head>
<body>

  <section class="card card--back" aria-label="Card back">
    <div class="firm-mark">
      <div class="firm-name">Harrow &amp; Vance</div>
      <div class="firm-tagline">A Professional Law Corporation</div>
    </div>
  </section>

  <section class="card card--front" aria-label="Card front">
    <div class="person">
      <div class="person-name">Owen Bartholomew Lindqvist</div>
      <div class="person-title">Attorney at Law</div>
      <div class="person-rule"></div>
      <ul class="contact-list">
        <li class="contact-item">
          <svg class="contact-icon" viewBox="0 0 24 24" aria-hidden="true"><path d="M6.6 10.8a15.1 15.1 0 0 0 6.6 6.6l2.2-2.2c.3-.3.7-.4 1-.2 1.1.4 2.3.6 3.6.6.6 0 1 .4 1 1V20c0 .6-.4 1-1 1A17 17 0 0 1 3 4c0-.6.4-1 1-1h3.5c.6 0 1 .4 1 1 0 1.3.2 2.5.6 3.6.1.3 0 .7-.2 1z"/></svg>
          (555) 214-3860
        </li>
        <li class="contact-item">
          <svg class="contact-icon" viewBox="0 0 24 24" aria-hidden="true"><path d="M6 2h12v6H6zM3 9h18v9h-3v4H6v-4H3zm5 6v5h8v-5z"/></svg>
          (555) 214-3861
        </li>
        <li class="contact-item">
          <svg class="contact-icon" viewBox="0 0 24 24" aria-hidden="true"><path d="M2 5h20v14H2zm2 2v.5l8 5.5 8-5.5V7zm0 3v7h16v-7l-8 5.5z"/></svg>
          olindqvist@harrowvance.com
        </li>
        <li class="contact-item">
          <svg class="contact-icon" viewBox="0 0 24 24" aria-hidden="true"><path d="M12 2a10 10 0 1 0 0 20 10 10 0 0 0 0-20zm6.9 6h-3a15 15 0 0 0-1.3-4A8 8 0 0 1 18.9 8zM12 4c.8 1.2 1.5 2.5 1.9 4h-3.8c.4-1.5 1.1-2.8 1.9-4zM4.3 14a8 8 0 0 1 0-4h3.4a16 16 0 0 0 0 4zm.8 2h3a15 15 0 0 0 1.3 4A8 8 0 0 1 5.1 16zm3-8h-3a8 8 0 0 1 4.3-4 15 15 0 0 0-1.3 4zM12 20c-.8-1.2-1.5-2.5-1.9-4h3.8c-.4 1.5-1.1 2.8-1.9 4zm2.3-6H9.7a14 14 0 0 1 0-4h4.6a14 14 0 0 1 0 4zm.3 6a15 15 0 0 0 1.3-4h3a8 8 0 0 1-4.3 4zm1.7-6a16 16 0 0 0 0-4h3.4a8 8 0 0 1 0 4z"/></svg>
          www.harrowvance.com
        </li>
      </ul>
    </div>

    <div class="firm-mark">
      <div class="firm-name">Harrow &amp; Vance</div>
      <div class="firm-tagline">A Professional Law Corporation</div>
    </div>

    <address class="address">
      4870 Alder Grove Lane, Suite 210<br>
      Fairmont Ridge, California 90417
    </address>
  </section>

</body>
</html>
```